Corvallin Property Solutions need a business card design

Hello guys. We would need a business card design asap please.
We are a start up property investment business based in London UK specialised in buying, selling, managing and letting properties and helping distressed property owners.
The name of our Business is Corvallin, the logo symbolises the four fundamental elements of the world (earth, air, fire and water) and so it stands for strength, stability, longevity.
We would like the business card to communicate professionalism and reliability. Many many thanks indeed for your work.

Details:

1.) Marisol Dunkley
Property Investor
Mobile: +44(0)7700362517
Email: marisol.corvallin@quilbrook.example

2.) Tomas Brindle
Property Investor
Mobile: +44(0)7700845926
Email: tomas.corvallin@quilbrook.example

Industry/Entity Type

Investment

```html
<!DOCTYPE html>
<html lang="en">
<head>
<meta charset="utf-8">
<title>Corvallin Property Solutions – Business Card</title>
<link rel="stylesheet" href="https://fonts.googleapis.com/css2?family=Josefin+Sans:wght@700&family=Roboto+Condensed:wght@300;400;700&display=swap">
<style>
  :root {
    --panel-black: #000000;
    --page-white: #ffffff;
    --brand-grey: #5a5a5a;
    --card-dark-top: #3a3a3a;
    --card-dark-bottom: #1c1c1c;
    --card-dark-text: #4c4c4c;
    --yellow-deep: #a88500;
    --yellow-mid: #dcb800;
    --yellow-bright: #f2e000;
    --ink-light: #ffffff;
  }
  * { margin: 0; padding: 0; box-sizing: border-box; }
  html, body { width: 1200px; height: 900px; overflow: hidden; background: var(--page-white); }
  .canvas { position: relative; width: 1200px; height: 900px; background: var(--page-white); }

  .brand-panel {
    position: absolute; left: 0; top: 0; width: 382px; height: 900px;
    background: var(--panel-black);
  }
  .brand-panel__mark {
    position: absolute; left: 150px; top: 360px; width: 96px; height: 96px;
    border-radius: 50%; background: #2a2a2a;
  }
  .wordmark {
    position: absolute; text-align: center;
    font-family: "Josefin Sans", sans-serif; font-weight: 700;
    text-transform: uppercase; line-height: 1;
  }
  .brand-panel .wordmark { left: 0; width: 396px; top: 512px; color: var(--brand-grey); }
  .brand-panel .wordmark__name { font-size: 25px; letter-spacing: 0.5px; display: block; }
  .brand-panel .wordmark__tag { font-size: 12px; letter-spacing: 0.6px; display: block; margin-top: 9px; }

  .card {
    position: absolute; border-radius: 28px; overflow: hidden;
    box-shadow: 0 14px 26px rgba(0,0,0,0.28);
  }
  .card--front {
    left: 495px; top: 76px; width: 602px; height: 342px;
    background: radial-gradient(ellipse at 50% 20%, var(--card-dark-top), var(--card-dark-bottom) 85%);
  }
  .card--front .wordmark { left: 0; width: 100%; top: 210px; color: var(--card-dark-text); }
  .card--front .wordmark__name { font-size: 52px; letter-spacing: 1px; display: block; }
  .card--front .wordmark__tag { font-size: 35px; letter-spacing: 0.8px; display: block; margin-top: 10px; }

  .card--back {
    left: 500px; top: 496px; width: 601px; height: 343px;
    background:
      radial-gradient(ellipse at 55% 95%, var(--yellow-bright), rgba(242,224,0,0) 60%),
      linear-gradient(180deg, var(--yellow-deep) 0%, var(--yellow-mid) 35%, var(--yellow-mid) 100%);
  }
  .card--back__mark {
    position: absolute; left: 104px; top: 58px; width: 110px; height: 110px;
    border-radius: 50%; background: rgba(255,255,255,0.28);
  }
  .card--back .wordmark { left: 40px; width: 236px; top: 220px; color: var(--ink-light); }
  .card--back .wordmark__name { font-size: 27px; letter-spacing: 0.4px; display: block; }
  .card--back .wordmark__tag { font-size: 13.5px; letter-spacing: 0.5px; display: block; margin-top: 9px; }

  .card--back__divider {
    position: absolute; left: 290px; top: 52px; width: 2px; height: 128px;
    background: var(--ink-light);
  }
  .contact {
    position: absolute; left: 336px; top: 80px; color: var(--ink-light);
    font-family: "Roboto Condensed", sans-serif;
  }
  .contact__name { font-weight: 700; font-size: 16px; line-height: 20px; }
  .contact__role { font-weight: 300; font-size: 14px; line-height: 20px; margin-top: 1px; }
  .contact__line {
    display: flex; align-items: center; gap: 4px;
    font-weight: 300; font-size: 12.5px; line-height: 18px;
  }
  .contact__line:first-of-type { margin-top: 6px; }
  .contact__icon { width: 12px; height: 12px; flex: none; }
</style>
</head>
<body>
<div class="canvas">

  <section class="brand-panel">
    <div class="brand-panel__mark"></div>
    <div class="wordmark">
      <span class="wordmark__name">Corvallin</span>
      <span class="wordmark__tag">Property Solutions</span>
    </div>
  </section>

  <section class="card card--front">
    <div class="wordmark">
      <span class="wordmark__name">Corvallin</span>
      <span class="wordmark__tag">Property&nbsp;&nbsp; Solutions</span>
    </div>
  </section>

  <section class="card card--back">
    <div class="card--back__mark"></div>
    <div class="wordmark">
      <span class="wordmark__name">Corvallin</span>
      <span class="wordmark__tag">Property Solutions</span>
    </div>
    <div class="card--back__divider"></div>
    <div class="contact">
      <p class="contact__name">Marisol Dunkley</p>
      <p class="contact__role">Property Investor</p>
      <p class="contact__line">
        <svg class="contact__icon" viewBox="0 0 12 12" aria-hidden="true"><circle cx="6" cy="6" r="5.3" fill="none" stroke="#fff" stroke-width="0.9"/><rect x="4.3" y="2.8" width="3.4" height="6.4" rx="0.7" fill="none" stroke="#fff" stroke-width="0.8"/></svg>
        +44(0)7700362517
      </p>
      <p class="contact__line">
        <svg class="contact__icon" viewBox="0 0 12 12" aria-hidden="true"><circle cx="6" cy="6" r="5.3" fill="none" stroke="#fff" stroke-width="0.9"/><rect x="3" y="4" width="6" height="4.2" fill="none" stroke="#fff" stroke-width="0.8"/><path d="M3 4 L6 6.4 L9 4" fill="none" stroke="#fff" stroke-width="0.8"/></svg>
        marisol.corvallin@quilbrook.example
      </p>
    </div>
  </section>

</div>
</body>
</html>
```